Tallowmere Fitness Business Card - I want exactly the same font than the font on the logo for my Name if possible and address and ETC. or a similar font that will look really good

I need those business cards ASAP so it would be amazing if you can submit your designs as quickly as possible!

Thanks so much

```html
<!DOCTYPE html>
<html lang="en">
<head>
<meta charset="utf-8">
<title>Tallowmere Fitness Business Card</title>
<link rel="stylesheet" href="https://fonts.googleapis.com/css2?family=Montserrat:wght@300;400;800&display=swap">
<style>
  :root {
    --bg: #e6e3df;
    --red: #b81d26;
    --red-dark: #8e1219;
    --black: #161616;
    --white: #f6f6f6;
    --ink: #1a1a1a;
    --grey: #555555;
    --font: "Montserrat", Arial, sans-serif;
  }
  * { margin: 0; padding: 0; box-sizing: border-box; }
  html, body { width: 1200px; height: 1000px; overflow: hidden; }
  body { background: var(--bg); font-family: var(--font); position: relative; }

  .card {
    position: absolute;
    width: 700px;
    height: 400px;
    overflow: hidden;
    box-shadow: 0 10px 30px rgba(0,0,0,0.18);
  }

  /* Front */
  .card--front { left: 70px; top: 60px; background: var(--white); }
  .front__band {
    position: absolute; left: 0; right: 0; bottom: 0; height: 180px;
    background: linear-gradient(90deg, var(--red) 0%, var(--red) 55%, var(--red-dark) 100%);
  }
  .front__logo {
    position: absolute; left: 0; right: 0; top: 150px;
    display: flex; align-items: center; justify-content: center; gap: 14px;
  }
  .logo-mark { width: 22px; height: 22px; background: var(--red); }
  .logo-name {
    font-weight: 800; font-size: 34px; letter-spacing: 1px;
    color: var(--ink); text-transform: uppercase;
  }

  /* Back */
  .card--back { left: 430px; top: 540px; background: var(--white); }
  .back__shapes { position: absolute; inset: 0; z-index: 0; }
  .back__logo {
    position: absolute; left: 40px; top: 168px; z-index: 1;
    font-weight: 800; font-size: 30px; line-height: 1.1;
    color: var(--white); text-transform: uppercase; letter-spacing: 1px;
  }
  .back__person {
    position: absolute; right: 40px; top: 34px; z-index: 1;
    text-align: right; color: var(--white);
  }
  .person__name { font-weight: 300; font-size: 30px; letter-spacing: 1px; }
  .person__role { font-weight: 300; font-size: 14px; margin-top: 6px; }

  .back__contact {
    position: absolute; right: 40px; top: 160px; z-index: 1;
    width: 300px; text-align: right; color: var(--ink);
  }
  .contact__brand {
    font-weight: 800; font-size: 22px; text-transform: uppercase; letter-spacing: 0.5px;
  }
  .contact__address { font-weight: 400; font-size: 10.5px; color: var(--grey); line-height: 1.45; margin-top: 4px; }
  .contact__phone { font-size: 13px; font-weight: 400; margin-top: 12px; display: flex; justify-content: flex-end; align-items: center; gap: 8px; }
  .phone-icon { width: 20px; height: 20px; }
  .contact__web { font-size: 11px; color: var(--grey); margin-top: 4px; }
  .contact__rule { height: 1px; background: var(--red); margin: 10px 0 12px 100px; }
  .contact__line { font-size: 11px; color: var(--grey); line-height: 1.6; }
</style>
</head>
<body>

  <section class="card card--front" aria-label="Business card front">
    <div class="front__logo">
      <span class="logo-mark"></span>
      <span class="logo-name">Tallowmere Fitness</span>
    </div>
    <div class="front__band"></div>
  </section>

  <section class="card card--back" aria-label="Business card back">
    <svg class="back__shapes" width="700" height="400" viewBox="0 0 700 400">
      <defs>
        <linearGradient id="redPanel" x1="0" y1="0" x2="1" y2="1">
          <stop offset="0" stop-color="#8e1219"/>
          <stop offset="0.5" stop-color="#b81d26"/>
          <stop offset="1" stop-color="#b81d26"/>
        </linearGradient>
      </defs>
      <polygon points="0,0 205,0 302,160 294,400 0,400" fill="url(#redPanel)"/>
      <polygon points="218,0 700,0 700,118 314,152" fill="#161616"/>
      <polygon role="img" aria-label="Mountain peak illustration" points="322,180 312,400 520,400" fill="#b81d26"/>
    </svg>

    <div class="back__logo">Tallowmere<br>Fitness</div>

    <div class="back__person">
      <div class="person__name">DANA ROWE</div>
      <div class="person__role">Strength &amp; Conditioning Coach</div>
    </div>

    <div class="back__contact">
      <div class="contact__brand">Tallowmere Fitness</div>
      <div class="contact__address">Harbour Point - Australia, Level 4,<br>58 Linden St., Eastvale VIC 3000</div>
      <div class="contact__phone">
        <span>0400 555 218</span>
        <svg class="phone-icon" viewBox="0 0 20 20" aria-hidden="true">
          <rect width="20" height="20" fill="#b81d26"/>
          <path d="M6 4.5 L8.2 4.5 L9 7.5 L7.6 8.6 Q8.8 11.2 11.4 12.4 L12.5 11 L15.5 11.8 L15.5 14 Q15.5 15.5 14 15.5 Q4.5 15 4.5 6 Q4.5 4.5 6 4.5 Z" fill="#ffffff"/>
        </svg>
      </div>
      <div class="contact__web">www.tallowmerefitness.com</div>
      <div class="contact__rule"></div>
      <div class="contact__line">drowe@tallowmerefitness.com</div>
      <div class="contact__line">social: /tallowmerefitness</div>
    </div>
  </section>

</body>
</html>
```